Need PressPad Blog Designed

I have just started a blog (www.velvetpantrybites.com), but I don't have a design background to make it look good.

Specifically I would like to add:

Top – Home, About, Contact

Sidebar – Categories, Blog Roll, Facebook, Twitter, Top Post, Tag Cloud, Recent Post, area to upload a video.

I would also like to normalize the font and the format and add cool buttons for links like the more button.

The colors chosen can be any of the colors used in the logo.

Other recommendations and changes are welcome as well.

Requirements
Must have
• Logo

```html
<!DOCTYPE html>
<html lang="en">
<head>
<meta charset="utf-8">
<title>Velvet Pantry Bites</title>
<link href="https://fonts.googleapis.com/css2?family=Questrial&family=Arimo:wght@400;700&display=swap" rel="stylesheet">
<style>
:root{
  --page:#ebe4e3;
  --band:#b9abb6;
  --pink:#d6336b;
  --pink-dark:#b22657;
  --brown:#3c2418;
  --brown-mid:#6b4024;
  --tan:#a4744e;
  --panel:#f6f4f4;
  --ink:#2a2a2a;
  --muted:#7a7474;
  --rule:#d6d0d0;
  --white:#ffffff;
  --accent:#f4a24a;
  --tag:#9a9494;
  --dark-btn:#1a1210;
}
*{margin:0;padding:0;box-sizing:border-box}
html,body{width:705px;height:1200px;overflow:hidden}
body{position:relative;background:var(--page);font-family:"Arimo",Arial,sans-serif;color:var(--ink)}
.abs{position:absolute}
.top-band{left:0;top:0;width:705px;height:20px;background:linear-gradient(90deg,#f3d86a,#e86a95,#9fd3cf,#f3d86a,#e86a95,#9fd3cf);opacity:.8}
.bottom-band{left:0;top:1105px;width:705px;height:95px;background:var(--band)}
.tagline{left:17px;top:32px;font-size:11px;color:var(--brown)}
.brand{left:17px;top:58px;display:flex;align-items:center;gap:10px}
.brand-mark{width:34px;height:34px;background:var(--pink);border-radius:4px}
.brand-name{font-family:"Questrial",sans-serif;font-size:28px;color:var(--brown)}
.account{right:45px;top:24px;font-size:9px;color:var(--pink)}
.account span{margin:0 8px;color:var(--muted)}
.search-field{left:458px;top:59px;width:127px;height:26px;background:var(--white);border-radius:3px}
.btn{background:var(--pink);color:var(--white);font-size:9px;border-radius:3px;display:flex;align-items:center;justify-content:center}
.search-btn{left:593px;top:59px;width:66px;height:26px}
.main-nav{left:40px;top:118px;width:620px;height:32px;background:linear-gradient(var(--pink),var(--pink-dark));border-radius:3px;display:flex;align-items:center;justify-content:center;font-family:"Questrial",sans-serif;font-size:11px;color:var(--white)}
.main-nav a{color:inherit;text-decoration:none;margin:0 12px}
.main-nav .current{color:var(--accent)}
.main-nav .sep{opacity:.8}
.hero{left:38px;top:158px;width:623px;height:231px;background:var(--white);box-shadow:0 6px 8px rgba(0,0,0,.15)}
.hero-fill{left:42px;top:162px;width:615px;height:223px;background:radial-gradient(circle at 70% 40%,#3a1e12,#6b3c22 45%,#c79a63 80%,#e2c28f)}
.promo{top:410px;width:199px;height:110px;clip-path:polygon(0 0,100% 0,100% 100%,50% 78%,0 100%);color:var(--white);padding:12px 7px}
.promo h2{font-family:"Questrial",sans-serif;font-weight:400;font-size:14px;margin-bottom:6px}
.promo p{font-size:7.3px;line-height:1.45}
.promo .more{position:absolute;right:6px;top:75px;background:var(--dark-btn);color:var(--white);font-size:7px;padding:4px 4px;border-radius:3px}
.promo-who{left:39px;background:var(--brown)}
.promo-what{left:249px;background:var(--pink)}
.promo-why{left:458px;background:var(--tan)}
.panel{left:39px;top:540px;width:621px;height:610px;background:var(--panel)}
.sidebar-rule{left:215px;top:545px;width:1px;height:595px;background:var(--rule)}
.side-head{left:43px;width:166px;height:28px;color:var(--white);font-family:"Questrial",sans-serif;font-size:14px;padding:6px 7px}
.cat-head{top:545px;background:linear-gradient(var(--pink),var(--pink-dark))}
.recent-head{top:738px;background:linear-gradient(var(--brown-mid),var(--brown))}
.cat-list{left:54px;top:580px;list-style:none;font-size:10.5px;line-height:17px}
.recent-list{left:41px;top:772px;width:168px;list-style:none;font-size:8.5px;line-height:17px}
.recent-list li{padding:2px 4px 7px;border-bottom:1px solid var(--rule);margin-bottom:6px;white-space:nowrap}
.recent-list li:last-child{border:0}
.tags{left:52px;top:1002px;width:160px;color:var(--tag);font-family:"Questrial",sans-serif;line-height:1.12;white-space:nowrap}
.tags .s{font-size:10px}
.tags .m{font-size:12.5px}
.tags .l{font-size:17px}
.tags .xl{font-size:20px}
.content{left:224px;top:553px;width:310px}
.page-title{font-family:"Questrial",sans-serif;font-weight:400;font-size:14px;margin-bottom:22px}
.content p{font-size:8.4px;line-height:1.3;margin-bottom:9px}
.drizzle{left:540px;top:540px;width:120px;height:255px;background:linear-gradient(160deg,#d9cfc9 0%,#6b3c22 35%,#4a2615 60%,#efe9e6 62%)}
.rule{height:1px;background:var(--rule)}
.post{left:223px;top:808px;width:432px}
.post h3{font-weight:400;font-size:9.5px;color:var(--brown);margin-bottom:8px;padding-left:2px}
.post .meta{font-size:7.5px;color:var(--muted);margin-bottom:8px;padding-left:2px}
.post-body{width:235px;font-size:8.4px;line-height:1.3}
.post-body p{margin-bottom:9px}
.post-photo{left:468px;top:842px;width:180px;height:120px;background:linear-gradient(135deg,#5c6f86,#b9a37a 50%,#2e3440)}
.read-more{left:400px;top:1011px;font-size:8.5px;color:var(--brown)}
.upload-title{left:222px;top:1037px;font-family:"Questrial",sans-serif;font-size:14px;font-weight:400}
.upload-field{left:222px;top:1061px;width:126px;height:26px;background:#d8d6d6;border-radius:3px}
.upload-btn{left:357px;top:1061px;width:66px;height:26px}
.embed-box{left:435px;top:1040px;width:213px;height:60px;background:#d6d4d4;border-radius:4px}
.embed-btn{left:580px;top:1107px;width:66px;height:26px}
.social{left:44px;top:1156px;display:flex;gap:5px}
.social i{width:20px;height:20px;border-radius:50%;display:block}
.footer-nav{left:187px;top:1165px;font-size:9.5px;color:#6d6268;font-family:"Questrial",sans-serif;white-space:nowrap}
.footer-nav span{margin:0 13px}
.footer-nav span:first-child{margin-left:0}
.footer-nav .current{color:var(--ink)}
.copyright{left:38px;top:1184px;font-size:7.5px;color:#5e5358}
</style>
</head>
<body>
<div class="abs top-band"></div>
<div class="abs bottom-band"></div>

<header>
  <p class="abs tagline">Your source for positive news stories in the black community</p>
  <div class="abs brand"><span class="brand-mark"></span><span class="brand-name">Velvet Pantry Bites</span></div>
  <div class="abs account">Login<span>|</span>Register</div>
  <div class="abs search-field"></div>
  <div class="abs btn search-btn">Search</div>
  <nav class="abs main-nav">
    <a class="current">Home</a><span class="sep">|</span><a>About us</a><span class="sep">|</span><a>Services</a><span class="sep">|</span><a>Products</a><span class="sep">|</span><a>Blog</a><span class="sep">|</span><a>Events</a><span class="sep">|</span><a>Community</a><span class="sep">|</span><a>Contact us</a>
  </nav>
</header>

<div class="abs hero"></div>
<div class="abs hero-fill" role="img" aria-label="Close-up of a chocolate chip and nut cookie bar"></div>

<section class="abs promo promo-who"><h2>Who we are?</h2><p>Lorem ipsum dolor sit amet, consectetuer adipiscing elit, sed diam nonummy nibh euismod tincidunt ut laoreet dolore magna aliquam erat volutpat.</p><span class="more">Read more</span></section>
<section class="abs promo promo-what"><h2>What we done?</h2><p>Lorem ipsum dolor sit amet, consectetuer adipiscing elit, sed diam nonummy nibh euismod tincidunt ut laoreet dolore magna aliquam erat volutpat.</p><span class="more">Read more</span></section>
<section class="abs promo promo-why"><h2>Why us?</h2><p>Lorem ipsum dolor sit amet, consectetuer adipiscing elit, sed diam nonummy nibh euismod tincidunt ut laoreet dolore magna aliquam erat volutpat.</p><span class="more">Read more</span></section>

<div class="abs panel"></div>
<div class="abs sidebar-rule"></div>

<aside>
  <div class="abs side-head cat-head">Categories</div>
  <ul class="abs cat-list">
    <li>Business</li><li>Community Giants</li><li>Feel Good Stories</li><li>Health</li><li>Our Youth</li><li>Politics</li><li>Sports</li><li>Taking Action</li><li>Uncategorized</li>
  </ul>
  <div class="abs side-head recent-head">Recent Posts</div>
  <ul class="abs recent-list">
    <li>Black Entrepreneurs Gain a Foothold in<br>&nbsp;&nbsp;&nbsp;Silicon Valley with LaunchNest group</li>
    <li>Darren Lockett voted into the Hall of Fame!</li>
    <li>Black Woman named to head Women in<br>&nbsp;&nbsp;&nbsp;Flight Board of Directors</li>
    <li>Celestine Moore, Marcus Pell's daughter,<br>&nbsp;&nbsp;&nbsp;gets new show on KidWave</li>
    <li>Black Fraternities Form Unity PAC</li>
  </ul>
  <div class="abs tags">
    <span class="s">apple pie</span> <span class="s">Bars</span> <span class="s">Biscuits</span> <span class="l">bread</span><br>
    <span class="s">bread machine</span><br>
    <span class="xl">breakfast</span> <span class="s">brownies</span><br>
    <span class="m">buns</span> <span class="l">cake</span> <span class="s">candy</span> <span class="m">caramel</span><br>
    <span class="m">cheese</span> <span class="xl">Chocolate</span><br>
    <span class="l">Christmas</span>
  </div>
</aside>

<div class="abs drizzle" role="img" aria-label="Melted chocolate dripping from a spoon"></div>

<main class="abs content">
  <h1 class="page-title">Welcome to Velvet Pantry Bites</h1>
  <p>This is an example page. It's different from a blog post because it will stay in one place and will show up in your site navigation (in most themes). Most people start with an About page that introduces them to potential site visitors. It might say something like this:</p>
  <p>&nbsp;&nbsp;&nbsp;Hi there! I'm a bike messenger by day, aspiring actor by night, and this is my blog. I live in Los Angeles, have a great dog named Jack, and I like piña coladas. (And gettin' caught in the rain.)</p>
  <p>…or something like this:</p>
  <p>&nbsp;&nbsp;&nbsp;The XYZ Doohickey Company was founded in 1971, and has been providing quality doohickies to the public ever since. Located in Gotham City, XYZ employs over 2,000 people and does all kinds of awesome things for the Gotham community.</p>
  <p>As a new PressPad user, you should go to your dashboard to delete this page and create new pages for your content. Have fun!</p>
</main>

<div class="abs rule" style="left:222px;top:795px;width:433px"></div>

<article class="abs post">
  <h3>Black Entrepreneurs Gain a Foothold in Silicon Valley with LaunchNest group</h3>
  <p class="meta">Posted on January 9, 2012 by admin</p>
  <div class="post-body">
    <p>When Calvin Brooks moved to Silicon Valley from Miami in 2010 to jump-start his Web business, his first goal was to join a community of fellow black entrepreneurs. "Then I realized there was no community," said Brooks, the CEO of website builder Gridwork Studio. Brooks is now a leader of the group Founders Circle, which works to create opportunities for African-Americans in technology.</p>
    <p>Silicon Valley is in need of such opportunities. California's cradle of innovation, while very good at spawning successful technology companies, is not so good at encouraging entrepreneurship among African-Americans. A recent report by VC Ledger, a venture capital information database, found that fewer than 1 percent of venture capital-backed tech companies in California were founded by African-Americans.</p>
  </div>
</article>
<div class="abs post-photo" role="img" aria-label="Two entrepreneurs talking at a tech meetup"></div>
<div class="abs read-more">Read more...</div>
<div class="abs rule" style="left:222px;top:1028px;width:433px"></div>

<h2 class="abs upload-title">Upload your video here</h2>
<div class="abs upload-field"></div>
<div class="abs btn upload-btn">Upload Video</div>
<div class="abs embed-box"></div>
<div class="abs btn embed-btn">Embed Object</div>

<footer>
  <div class="abs social">
    <i style="background:#3b5b98"></i><i style="background:#4aaee0"></i><i style="background:#c9302c"></i><i style="background:#f08a24"></i>
  </div>
  <div class="abs footer-nav"><span class="current">Home</span>|<span>About us</span>|<span>Services</span>|<span>Products</span>|<span>Blog</span>|<span>Events</span>|<span>Community</span>|<span>Contact us</span></div>
  <p class="abs copyright">© All Copyrights Reserved by Velvet Pantry Bites</p>
</footer>
</body>
</html>
```